Private Maths Tuition Flyer based in London

I am opening up a new Maths tuition centre in North West London. The flyer will be delivered to over 8,000 homes within the immediate vicinity. The design should be suitable to be printed on an A5 sheet and read in a portrait orientation.

The flyer should include the following:

The headline statement should be "Private Maths Tuition"

Secondary headline statement is the following "GCSE, A-Levels, 11 Plus exams"

Some of service offerings/selling points are:

- Free first session
- Monthly Feedback reports
- Free support outside of sessions
- Clear Target grades
- Personalised Lesson plans
- Tangible Results

Another statement that should be featured is "Book your free session by visiting www.lernova.co.uk" or something similar to that.

"Contact Details:
020 4719 8263
enquiries@lernova.co.uk"

"Address:
Kelbridge Business and Innovation Centre
Ashvale Court
Wrenfield Road
HA4 9QD"

Attached you'll see a logo which should be included and also a map of where we are. I am open to new images for the map if you guys have any, rather than a screen shot from google maps but it should be clear to see.

I would like the content above to be displayed in a clear and concise manner that is easy to read. You have creative license on where this information should be displayed and where the images should be but on the whole it should look aesthetically pleasing on the eye.

Target Market(s)

Students, Parents. Parents who want maths tutors.

Industry/Entity Type

Tutoring

Font styles to use
Sans Serif

Requirements
Must have
• *logo*
• Private Maths Tuition
• GCSE, A-Levels, 11 Plus exams
• - Free first session
• - Monthly Feedback reports
• - Free support outside of sessions
• - Clear Target grades
• - Personalised Lesson plans
• - Tangible Results
• Book your free session by visiting www.lernova.co.uk" or something similar to that.
• Contact Details:
• 020 4719 8263
• enquiries@lernova.co.uk
• Address (*with map*):
• Kelbridge Business and Innovation Centre
• Ashvale Court
• Wrenfield Road
• HA4 9QD
Nice to have
• similar colour scheme as the logo. creative background design.

```html
<!DOCTYPE html>
<html lang="en">
<head>
<meta charset="utf-8">
<title>Private Maths Tuition Flyer</title>
<link href="https://fonts.googleapis.com/css2?family=Ubuntu:wght@500;700&family=Play:wght@700&family=Lato:wght@400;700&display=swap" rel="stylesheet">
<style>
  :root {
    --blue: #1a5cac;
    --blue-deep: #0f4a96;
    --orange: #ec6a1e;
    --orange-deep: #c8520f;
    --leaf: #5aa62c;
    --ink: #262626;
    --panel-light: #ffffff;
    --panel-grey: #d9d9d9;
    --page-bg: #e9e6e1;
  }
  * { margin: 0; padding: 0; box-sizing: border-box; }
  html, body { width: 1200px; height: 1013px; overflow: hidden; background: var(--page-bg); }
  .flyer {
    position: absolute; left: 260px; top: 26px; width: 680px; height: 960px;
    background: var(--panel-light); overflow: hidden;
    font-family: "Lato", sans-serif; color: var(--ink);
    box-shadow: 0 4px 18px rgba(0,0,0,.18);
  }
  .flyer__title {
    position: absolute; top: 14px; width: 100%; text-align: center;
    font-family: "Ubuntu", sans-serif; font-weight: 700; font-size: 55px;
    color: var(--blue); letter-spacing: .5px;
  }
  .flyer__subtitle {
    position: absolute; top: 80px; width: 100%; text-align: center;
    font-family: "Lato", sans-serif; font-weight: 700; font-size: 30px; color: var(--orange);
  }
  .flyer__photo {
    position: absolute; left: 70px; top: 130px; width: 540px; height: 420px;
    background: radial-gradient(ellipse at 50% 45%, #e8c9a8 0%, #d9a47e 35%, #8aa0c0 70%, #ffffff 100%);
    border-radius: 40% 40% 0 0;
  }
  .flyer__waves { position: absolute; left: 0; top: 0; width: 680px; height: 960px; }
  .heading {
    font-family: "Play", sans-serif; font-weight: 700; color: var(--blue); font-size: 28px; line-height: 1.2;
  }
  .offerings { position: absolute; left: 22px; top: 560px; }
  .offerings__list { list-style: none; margin-top: 8px; }
  .offerings__item { display: flex; align-items: center; gap: 9px; height: 31px; font-size: 17.5px; }
  .divider { position: absolute; left: 323px; top: 578px; width: 2px; height: 250px;
    background: linear-gradient(#bdbdbd, #8a8a8a, #bdbdbd); }
  .booking { position: absolute; left: 358px; top: 562px; }
  .contact-line { display: flex; align-items: center; gap: 14px; font-size: 20px; margin-top: 6px; height: 28px; }
  .contact { position: absolute; left: 358px; top: 676px; }
  .address { position: absolute; left: 24px; top: 780px; }
  .address__body { display: flex; gap: 10px; margin-top: 6px; font-size: 17.5px; line-height: 21.5px; }
  .address__name { font-weight: 700; }
  .map {
    position: absolute; left: 262px; top: 805px; width: 156px; height: 156px; border-radius: 50%;
    border: 4px solid var(--orange); box-shadow: inset 0 0 0 3px #fff, inset 0 0 0 6px var(--blue);
    background: linear-gradient(135deg, #e6e2da 0%, #d6d2c9 50%, #cfe0bc 100%);
  }
  .brand { position: absolute; left: 455px; top: 872px; display: flex; align-items: center; gap: 10px; }
  .brand__mark { width: 22px; height: 22px; border-radius: 50%; background: var(--blue); }
  .brand__name { font-family: "Ubuntu", sans-serif; font-weight: 500; font-size: 44px; color: var(--orange); }
  .footer-band { position: absolute; left: 0; bottom: 0; width: 100%; height: 14px; background: var(--blue); }
</style>
</head>
<body>
<main class="flyer">
  <h1 class="flyer__title">Private Maths Tuition</h1>
  <p class="flyer__subtitle">GCSE, A-Levels, 11 Plus exams</p>

  <div class="flyer__photo" role="img" aria-label="Photo of a smiling group of five students holding notebooks"></div>

  <svg class="flyer__waves" viewBox="0 0 680 960" aria-hidden="true">
    <defs>
      <linearGradient id="panelFill" x1="0" y1="0" x2="0" y2="1">
        <stop offset="0" stop-color="#ffffff"/>
        <stop offset="1" stop-color="#d6d6d6"/>
      </linearGradient>
      <linearGradient id="orangeFill" x1="0" y1="0" x2="1" y2="0">
        <stop offset="0" stop-color="#c8520f"/>
        <stop offset=".5" stop-color="#ef7424"/>
        <stop offset="1" stop-color="#c8520f"/>
      </linearGradient>
    </defs>
    <path d="M0 420 C120 390 230 420 330 480 C430 540 560 540 680 440 L680 960 L0 960 Z" fill="#1a5cac"/>
    <path d="M0 448 C120 410 240 440 340 495 C450 560 580 560 680 470 L680 960 L0 960 Z" fill="#ffffff"/>
    <path d="M0 478 C120 440 250 470 360 520 C470 570 600 575 680 505 L680 960 L0 960 Z" fill="url(#orangeFill)"/>
    <path d="M0 510 C130 470 260 500 380 545 C490 585 610 590 680 560 L680 960 L0 960 Z" fill="url(#panelFill)"/>
  </svg>

  <section class="offerings">
    <h2 class="heading">Service Offerings</h2>
    <ul class="offerings__list">
      <li class="offerings__item"><svg width="18" height="14" viewBox="0 0 18 14"><path d="M1 1 C10 0 17 4 16 13 C8 13 2 9 1 1 Z" fill="var(--leaf)"/></svg>Free first session</li>
      <li class="offerings__item"><svg width="18" height="14" viewBox="0 0 18 14"><path d="M1 1 C10 0 17 4 16 13 C8 13 2 9 1 1 Z" fill="var(--leaf)"/></svg>Monthly Feedback reports</li>
      <li class="offerings__item"><svg width="18" height="14" viewBox="0 0 18 14"><path d="M1 1 C10 0 17 4 16 13 C8 13 2 9 1 1 Z" fill="var(--leaf)"/></svg>Free support outside of sessions</li>
      <li class="offerings__item"><svg width="18" height="14" viewBox="0 0 18 14"><path d="M1 1 C10 0 17 4 16 13 C8 13 2 9 1 1 Z" fill="var(--leaf)"/></svg>Clear Target grades</li>
      <li class="offerings__item"><svg width="18" height="14" viewBox="0 0 18 14"><path d="M1 1 C10 0 17 4 16 13 C8 13 2 9 1 1 Z" fill="var(--leaf)"/></svg>Personalised Lesson plans</li>
      <li class="offerings__item"><svg width="18" height="14" viewBox="0 0 18 14"><path d="M1 1 C10 0 17 4 16 13 C8 13 2 9 1 1 Z" fill="var(--leaf)"/></svg>Tangible Results</li>
    </ul>
  </section>

  <div class="divider"></div>

  <section class="booking">
    <h2 class="heading">Book your<br>free session by visiting</h2>
    <p class="contact-line"><svg width="16" height="16" viewBox="0 0 16 16"><circle cx="8" cy="8" r="7" fill="none" stroke="var(--leaf)" stroke-width="2"/><path d="M1 8 H15 M8 1 C4 5 4 11 8 15 M8 1 C12 5 12 11 8 15" stroke="var(--leaf)" stroke-width="1.4" fill="none"/></svg>www.lernova.co.uk</p>
  </section>

  <section class="contact">
    <h2 class="heading">Contact Details:</h2>
    <p class="contact-line"><svg width="16" height="18" viewBox="0 0 16 18"><path d="M3 1 L6 1 L7 5 L5 7 C6 10 8 12 10 13 L12 11 L15 12 L15 16 C8 17 1 10 3 1 Z" fill="var(--leaf)"/></svg>020 4719 8263</p>
    <p class="contact-line"><svg width="18" height="13" viewBox="0 0 18 13"><rect x="1" y="1" width="16" height="11" fill="var(--leaf)"/><path d="M1 1 L9 7 L17 1" stroke="#fff" stroke-width="1.5" fill="none"/></svg>enquiries@lernova.co.uk</p>
  </section>

  <section class="address">
    <h2 class="heading">Address:</h2>
    <div class="address__body">
      <svg width="14" height="20" viewBox="0 0 14 20"><path d="M7 19 C2 12 1 9 1 7 A6 6 0 0 1 13 7 C13 9 12 12 7 19 Z" fill="var(--leaf)"/><circle cx="7" cy="7" r="2.3" fill="#fff"/></svg>
      <p><span class="address__name">Kelbridge Business and<br>Innovation Centre</span><br>Ashvale Court<br>Wrenfield Road<br>HA4 9QD</p>
    </div>
  </section>

  <div class="map" role="img" aria-label="Street map showing the centre's location"></div>

  <div class="brand">
    <span class="brand__mark"></span>
    <span class="brand__name">Lernova</span>
  </div>

  <div class="footer-band"></div>
</main>
</body>
</html>
```